3 Flyer Project: Industrial, Civil, and Commercial

Total of 3 separate flyers that go together to be put in folders for marketing. The three flyer categories will be Industrial, Civil, and Commercial. I will upload three photos for each flyer and verbiage for each flyer. The photos may change upon final revisions. We want creativity and not just bullet points on a page.

FLYER #1 INDUSTRIAL

INDUSTRIAL EXPERIENCE:
BRAVEMOOR UTILITIES
VELKAR
GRAYWICK QUARRY
ODELL FORGEWORKS
PELLMAN CRYSTALLINE
HARROWGATE & DUNMORE RAIL LINE

INDUSTRIAL FOCUS AREAS:
PLANT FACILITY WATER SYSTEMS
HEAVY CONCRETE
FACILITY REPAIR
INDUSTRIAL UPGRADES
RAILWAYS AND MANUFACTURING

INDUSTRIAL SOLUTIONS:
WE MAINTAIN AN EXTENSIVE LEVEL OF DETAIL AND INNOVATIVE PROBLEM-SOLVING TALENTS TO DELIVER HIGH QUALITY, SUSTAINABLE SOLUTIONS.

FLYER #2 CIVIL

CIVIL EXPERIENCE:
CORVANE DEPT. OF TRANSPORTATION
WEXLOW DEPT. OF TRANSPORTATION
TAVERLY DEPT. OF TRANSPORTATION
BUILDERS GUILD BOARD
NATIONAL FLIGHT SAFETY OFFICE
MINISTRY OF GUARDIANSHIP

CIVIL FOCUS AREAS:
AIRFIELD
STREETSCAPES
STORM DRAINAGE
UTILITY UPGRADES
BOX CULVERTS
RETAINING WALLS

CIVIL SOLUTIONS:
WE SPECIALIZE IN COMPLEX CIVIL PROJECTS.

FLYER #3 COMMERCIAL

COMMERCIAL EXPERIENCE:
HOLLISTER VALE UNIVERSITY
CORVANE OFFICE OF FACILITIES
TOWN OF BRANWICK, CORVANE
TOWN OF ELDERMOOR, CORVANE
ACADEMIC REGENTS COUNCIL

COMMERCIAL FOCUS AREAS:
NEW CONSTRUCTION
RENOVATIONS
STRUCTURAL FOUNDATIONS
STRUCTURAL UPGRADES

COMMERCIAL SOLUTIONS:
WE NOT ONLY KNOW HOW ALL THE PARTS AND PIECES FIT TOGETHER WITHIN A PROJECT, BUT WE SPECIALIZE IN THE SELF PERFORMANCE OF MANY DIVISIONS WHICH DIFFERENTIATES US FROM MANY OTHER GENERAL CONTRACTORS.

Marketing

• 3 photos on each flyer based on the Industrial, Commercial, and Civil flyers description. Our company logo as well as descriptions shown for each flyer. The blue we use in our logo cmyk is 100-80-0-22

```html
<!DOCTYPE html>
<html lang="en">
<head>
<meta charset="utf-8">
<title>Hartwell Construction – Industrial Flyer</title>
<link rel="stylesheet" href="https://fonts.googleapis.com/css2?family=Oswald:wght@500;600&family=Lato:wght@400;700&display=swap">
<style>
  :root {
    --brand-blue: #26408f;
    --ink-gray: #474747;
    --text-dark: #222;
    --band-gray: #d3d2d4;
    --page-bg: #e9e9e9;
    --white: #fff;
  }
  * { box-sizing: border-box; margin: 0; padding: 0; }
  html, body { width: 1200px; height: 1200px; overflow: hidden; background: var(--page-bg); }
  .canvas { position: relative; width: 1200px; height: 1200px; }
  .flyer {
    position: absolute; left: 171px; top: 44px;
    width: 894px; height: 1158px; background: var(--white);
    transform: scale(0.96); transform-origin: 0 0;
    font-family: "Lato", sans-serif; overflow: hidden;
    box-shadow: 0 4px 18px rgba(0,0,0,.18);
  }
  .hero { position: absolute; left: 0; top: 0; width: 894px; height: 530px; }
  .headline { position: absolute; top: 40px; left: 0; width: 100%; text-align: center; font-family: "Oswald", sans-serif; font-weight: 600; line-height: 1; }
  .headline__main { font-size: 50px; color: var(--ink-gray); letter-spacing: 1px; }
  .headline__sub { font-size: 48px; color: var(--brand-blue); margin-top: 0; letter-spacing: 1px; }

  .brand { position: absolute; left: 174px; top: 516px; display: flex; align-items: center; gap: 14px; }
  .brand__mark { width: 70px; height: 80px; background: var(--brand-blue); }
  .brand__name { font-family: "Oswald", sans-serif; font-weight: 600; color: var(--brand-blue); line-height: 1; }
  .brand__name span { display: block; }
  .brand__name .top { font-size: 60px; letter-spacing: 0; }
  .brand__name .bottom { font-size: 22px; letter-spacing: 1.5px; margin-top: 2px; }

  .section-title { position: absolute; left: 35px; font-size: 23px; font-weight: 400; letter-spacing: .3px; }
  .focus-title { top: 649px; color: var(--text-dark); }
  .experience-title { top: 946px; color: var(--brand-blue); }

  .focus-list { position: absolute; left: 36px; top: 698px; list-style: none; }
  .focus-list li { display: flex; align-items: center; height: 43.5px; font-size: 18px; color: var(--text-dark); }
  .focus-list svg { width: 30px; height: 30px; margin-right: 25px; flex: none; }

  .partners { position: absolute; left: 30px; top: 985px; width: 490px; display: flex; justify-content: space-between; align-items: center; }
  .partners li { list-style: none; font-size: 9.5px; font-weight: 700; line-height: 1.15; color: var(--brand-blue); text-align: center; width: 74px; }

  .photo { position: absolute; left: 532px; width: 362px; }
  .photo--night { top: 375px; height: 214px; background: linear-gradient(180deg, #1d2535 0%, #3a3a2e 55%, #8a6a3e 100%); }
  .photo--forms { top: 859px; height: 203px; background: linear-gradient(180deg, #8aa86a 0%, #c9a26b 35%, #b8864e 100%); }
  .gray-band { position: absolute; left: 532px; width: 362px; height: 15px; background: var(--band-gray); }

  .solutions { position: absolute; left: 532px; top: 617px; width: 362px; height: 215px; background: var(--brand-blue); color: var(--white); text-align: center; padding-top: 36px; }
  .solutions h2 { font-family: "Lato", sans-serif; font-weight: 400; font-size: 34px; line-height: 1.22; letter-spacing: .5px; }
  .solutions p { font-size: 13.5px; line-height: 1.3; margin: 22px 28px 0; }

  .footer-rule { position: absolute; left: 0; top: 1067px; width: 100%; height: 5px; background: var(--brand-blue); }
  .footer-rule--gray { top: 1073px; height: 8px; background: var(--band-gray); }
  .footer { position: absolute; left: 0; top: 1082px; width: 100%; height: 76px; background: var(--brand-blue); color: var(--white); display: flex; align-items: center; padding-left: 35px; font-size: 14px; font-weight: 700; }
  .footer__item { display: flex; align-items: center; gap: 10px; margin-right: 28px; }
  .footer__item svg { width: 20px; height: 20px; }
</style>
</head>
<body>
<div class="canvas">
  <article class="flyer">
    <svg class="hero" viewBox="0 0 894 530" aria-hidden="false">
      <defs>
        <linearGradient id="heroFill" x1="0" y1="0" x2="0" y2="1">
          <stop offset="0" stop-color="#f4f7fb"/>
          <stop offset="0.35" stop-color="#b9cfe6"/>
          <stop offset="0.6" stop-color="#9fa3a0"/>
          <stop offset="0.8" stop-color="#6f8f55"/>
          <stop offset="1" stop-color="#4d7a36"/>
        </linearGradient>
      </defs>
      <polygon role="img" aria-label="Photo of a power plant with cooling towers and smokestacks under a cloudy sky" points="0,0 894,0 894,352 475,362 102,517 0,462" fill="url(#heroFill)"/>
      <polyline points="0,466 102,521 475,366 894,357" fill="none" stroke="var(--brand-blue)" stroke-width="7"/>
      <rect x="475" y="358" width="419" height="6" fill="var(--brand-blue)"/>
    </svg>

    <header class="headline">
      <div class="headline__main">QUALITY CONSTRUCTION</div>
      <div class="headline__sub">First Class Delevery</div>
    </header>

    <div class="brand">
      <div class="brand__mark"></div>
      <div class="brand__name"><span class="top">HARTWELL</span><span class="bottom">CONSTRUCTION</span></div>
    </div>

    <h2 class="section-title focus-title">INDUSTRIAL FOCUS AREAS:</h2>
    <ul class="focus-list">
      <li><svg viewBox="0 0 30 30"><path d="M6 4h12v4h-4v6H10V8H6z M4 20c3-2 5 2 8 0s5 2 8 0 5 2 7 0 M4 25c3-2 5 2 8 0s5 2 8 0 5 2 7 0" fill="none" stroke="#555" stroke-width="1.6"/></svg>Plant Facility Water Systems</li>
      <li><svg viewBox="0 0 30 30"><path d="M4 9l11-5 11 5v12l-11 5-11-5z" fill="#8d8d8d"/><path d="M4 9l11 5 11-5M15 14v12" fill="none" stroke="#444" stroke-width="1.5"/></svg>Heavy Concrete</li>
      <li><svg viewBox="0 0 30 30"><path d="M22 3a6 6 0 0 0-6 8L4 23l3 3 12-12a6 6 0 0 0 8-6l-4 2-3-3z" fill="#444"/></svg>Facility Repair</li>
      <li><svg viewBox="0 0 30 30"><path d="M3 26V14l6-4v4l6-4v4l6-4V4h4v22z" fill="none" stroke="#666" stroke-width="1.4"/></svg>Industrial Upgrades</li>
      <li><svg viewBox="0 0 30 30"><path d="M5 6l19 19M25 6L6 25" stroke="#333" stroke-width="3.5" stroke-linecap="round"/></svg>Railways and Manufacturing</li>
    </ul>

    <h2 class="section-title experience-title">INDUSTRIAL EXPERIENCE:</h2>
    <ul class="partners">
      <li>HARROWGATE &amp; DUNMORE RAIL LINE</li>
      <li>PELLMAN CRYSTALLINE</li>
      <li>ODELL FORGEWORKS</li>
      <li>GRAYWICK QUARRY</li>
      <li>VELKAR</li>
      <li>BRAVEMOOR UTILITIES</li>
    </ul>

    <div class="photo photo--night" role="img" aria-label="Photo of a night concrete pour at an industrial site with a pump truck and work lights"></div>
    <div class="gray-band" style="top:597px"></div>
    <section class="solutions">
      <h2>INDUSTRIAL<br>SOLUTIONS:</h2>
      <p>we maintain an extensive level of detail and innovative problem-solving talents to deliver high quality, sustainable solutions.</p>
    </section>
    <div class="gray-band" style="top:837px"></div>
    <div class="photo photo--forms" role="img" aria-label="Photo of timber concrete formwork for a large foundation on red clay"></div>

    <div class="footer-rule"></div>
    <div class="footer-rule footer-rule--gray"></div>
    <footer class="footer">
      <div class="footer__item"><svg viewBox="0 0 20 20"><path d="M10 2L1 10h3v8h5v-5h2v5h5v-8h3z" fill="#fff"/></svg>2280 Foundry Park Road Branwick, Corvane 40812</div>
      <div class="footer__item"><svg viewBox="0 0 20 20"><circle cx="10" cy="10" r="8" fill="none" stroke="#fff" stroke-width="1.5"/><path d="M2 10h16M10 2c-4 4-4 12 0 16M10 2c4 4 4 12 0 16" fill="none" stroke="#fff" stroke-width="1.3"/></svg><span style="font-weight:400">www.hartwellconstruction.com</span></div>
      <div class="footer__item"><svg viewBox="0 0 20 20"><path d="M4 2l3 0 1 4-2 1.5c1 2.5 3 4.5 5.5 5.5L13 11l4 1v3c0 1-1 2-2 2C8 17 3 12 3 5c0-1 0-3 1-3z" fill="#fff"/></svg>555-014-2290</div>
    </footer>
  </article>
</div>
</body>
</html>
```